Business Card Design for Property Development Company Director

I am looking for a professional and unforgettable business card design for our Director of our Property Development Company.
Please see attached .pptx file to find out what information to include. You don't have to follow the exact format shown in the file - I am interested to see your creative flair using the information provided.

```html
<!DOCTYPE html>
<html lang="en">
<head>
<meta charset="utf-8">
<title>Northvale Property Group – Business Card</title>
<link href="https://fonts.googleapis.com/css2?family=Montserrat:wght@400;500;600;700&display=swap" rel="stylesheet">
<style>
  :root {
    --page-bg: #eef0f3;
    --card-white: #f7f8f9;
    --brand-blue: #1f5ea8;
    --deep-blue: #1553a3;
    --brand-grey: #5e6266;
    --text-dark: #222426;
    --shadow: rgba(0, 0, 0, 0.28);
  }
  * { box-sizing: border-box; margin: 0; padding: 0; }
  html, body {
    width: 960px; height: 1200px; overflow: hidden;
    background: var(--page-bg);
    font-family: "Montserrat", Arial, sans-serif;
  }
  .sheet {
    position: relative; width: 960px; height: 1200px;
    display: flex; flex-direction: column; align-items: center;
    justify-content: center; gap: 70px;
  }
  .card {
    position: relative; width: 820px; height: 466px; overflow: hidden;
    box-shadow: 3px 4px 6px var(--shadow);
  }

  /* Front */
  .card-front { background: var(--card-white); }
  .monogram-area {
    position: absolute; right: 0; top: 0; width: 470px; height: 466px;
  }
  .front-content { position: absolute; left: 50px; top: 92px; }
  .wordmark { display: flex; align-items: center; gap: 12px; }
  .wordmark-square {
    width: 42px; height: 42px; background: var(--brand-grey);
  }
  .wordmark-text {
    color: var(--brand-grey); font-weight: 700; line-height: 1;
  }
  .wordmark-text .name { font-size: 34px; letter-spacing: 0.5px; display: block; }
  .wordmark-text .sub { font-size: 12px; letter-spacing: 3.4px; display: block; margin-top: 4px; }

  .person { margin-top: 42px; }
  .person-name { color: var(--deep-blue); font-size: 27px; font-weight: 600; }
  .person-role { color: var(--text-dark); font-size: 18px; font-weight: 400; margin-top: 2px; }

  .contacts { list-style: none; margin-top: 26px; }
  .contacts li {
    display: flex; align-items: center; gap: 8px;
    color: var(--text-dark); font-size: 19px; line-height: 30px;
  }
  .contacts svg { width: 12px; height: 12px; flex: none; }
  .licence { color: var(--text-dark); font-size: 15px; margin-top: 14px; }

  /* Back */
  .card-back {
    background: var(--brand-blue); color: #fff;
    display: flex; flex-direction: column; align-items: center;
  }
  .card-back .wordmark { margin-top: 196px; }
  .card-back .wordmark-square { background: #fff; width: 46px; height: 46px; }
  .card-back .wordmark-text { color: #fff; }
  .card-back .wordmark-text .name { font-size: 38px; }
  .tagline {
    margin-top: 62px; text-align: center; font-size: 19px;
    font-weight: 500; line-height: 24px;
  }
  .invite { margin-top: 26px; font-size: 12px; font-weight: 400; }
</style>
</head>
<body>
<main class="sheet">

  <section class="card card-front" aria-label="Business card front">
    <svg class="monogram-area" viewBox="0 0 470 466" role="img" aria-label="Large brand monogram decoration in blue and grey">
      <defs>
        <linearGradient id="monogramFill" x1="0" y1="1" x2="1" y2="0">
          <stop offset="0" stop-color="#1553a3"/>
          <stop offset="1" stop-color="#5e6266"/>
        </linearGradient>
      </defs>
      <polygon points="470,0 200,0 0,466 470,466" fill="url(#monogramFill)" opacity="0.92"/>
    </svg>

    <div class="front-content">
      <div class="wordmark">
        <span class="wordmark-square" aria-hidden="true"></span>
        <span class="wordmark-text">
          <span class="name">NORTHVALE</span>
          <span class="sub">PROPERTY GROUP</span>
        </span>
      </div>

      <div class="person">
        <p class="person-name">Daniel Marsh</p>
        <p class="person-role">Director</p>
      </div>

      <ul class="contacts">
        <li>
          <svg viewBox="0 0 12 12" aria-hidden="true"><path d="M3 1 L5 3.5 L4 5 Q5.5 7 7 8 L8.5 7 L11 9 L10 11 Q5 11 1 4 Z" fill="#1553a3"/></svg>
          0400-318-226
        </li>
        <li>
          <svg viewBox="0 0 12 12" aria-hidden="true"><rect x="1" y="2.5" width="10" height="7" fill="#1553a3"/><path d="M1 2.5 L6 6.5 L11 2.5" stroke="#fff" stroke-width="1" fill="none"/></svg>
          daniel@northvale.com.au
        </li>
        <li>
          <svg viewBox="0 0 12 12" aria-hidden="true"><circle cx="6" cy="6" r="5" fill="#8fb0d8"/></svg>
          www.northvale.com.au
        </li>
      </ul>
      <p class="licence">Real Estate Lic: 5127390 &amp; 5127391</p>
    </div>
  </section>

  <section class="card card-back" aria-label="Business card back">
    <div class="wordmark">
      <span class="wordmark-square" aria-hidden="true"></span>
      <span class="wordmark-text">
        <span class="name">NORTHVALE</span>
        <span class="sub">PROPERTY GROUP</span>
      </span>
    </div>
    <p class="tagline">Property Development<br>&amp; Site Acquisition Specialists</p>
    <p class="invite">Ask me about our INVESTMENT &amp; PARTNERSHIP opportunities</p>
  </section>

</main>
</body>
</html>
```